Car wellness, we make cars new and shiny

We need an design for a "small" ad that is published inside a magazine on a holiday tour bus. The audience is mostly 60+ years old.
We are a tinsmith's workshop and painter's shop company with a passion for shiny cars. We love to fix all the little scratches and dents a car gets over time and make it look new again.
The motto is car wellness (Wellness für Ihr Auto).
The ad has to be in German. If you are not fluent in German you may use the text in the example but feel free to use an appropriate font.
The COUPON is our call to action: We want the customer to call us. And it includes an offering of free get and return service of the customers car. It also inclueds some restrictions to the free service (proximity and valid until date).
Things that can't be changed are:
- the logo itself (the position, size and orientation are free)
- the color of the dot in the logo
- the size of the ad: 82mm x 118mm
- the magazines size: approx. A4
We expect a print ready result and would like to receive the files in original file format (eps, svg ...).
We hope for an eye-catching ad that drives the attention of the reader.
Car owners, with 60+ years of age.

```html
<!DOCTYPE html>
<html lang="de">
<head>
<meta charset="utf-8">
<title>Wellness für Ihr Auto – Anzeige</title>
<link rel="stylesheet" href="https://fonts.googleapis.com/css2?family=Exo+2:ital,wght@1,900&family=Montserrat:ital,wght@0,600;0,700;1,800&family=Open+Sans:wght@400;700&display=swap">
<style>
  :root {
    --orange: #e85d25;
    --orange-dark: #c9431e;
    --ink: #111111;
    --brand-ink: #2b2b2b;
    --paper: #ffffff;
    --pale: #f3f3f3;
    --frame: #333333;
  }
  * { margin: 0; padding: 0; box-sizing: border-box; }
  html, body { width: 1200px; height: 1000px; overflow: hidden; background: var(--paper); }
  .ad {
    position: absolute; left: 281px; top: 73px; width: 603px; height: 867px;
    border: 1.5px solid var(--frame); background: var(--paper); overflow: hidden;
  }
  .ad-backdrop { position: absolute; inset: 0; }
  .brand {
    position: absolute; top: 40px; left: 0; width: 100%; text-align: center;
    font-family: "Montserrat", sans-serif; font-weight: 600; font-size: 32px;
    color: var(--brand-ink); letter-spacing: 0;
  }
  .car-visual {
    position: absolute; left: 17px; top: 200px; width: 586px; height: 226px;
    border-radius: 36px;
    background: radial-gradient(ellipse at 55% 45%, #e23a40 0%, #bb1a22 60%, #8a1016 100%);
  }
  .headline {
    position: absolute; top: 462px; left: 0; width: 100%; text-align: center;
    font-family: "Exo 2", sans-serif; font-style: italic; font-weight: 900;
    font-size: 90px; line-height: 1; color: var(--orange); letter-spacing: 2px;
  }
  .subline {
    position: absolute; top: 546px; left: 0; width: 100%; text-align: center;
    font-family: "Montserrat", sans-serif; font-style: italic; font-weight: 800;
    font-size: 47px; line-height: 1; color: var(--ink);
  }
  .lead {
    position: absolute; top: 599px; left: 0; width: 100%; text-align: center;
    font-family: "Open Sans", sans-serif; font-size: 18.5px; line-height: 25px; color: var(--ink);
  }
  .coupon-cut {
    position: absolute; left: 22px; top: 662px; width: 557px; height: 182px;
    border: 1.5px dashed #9a9a9a;
  }
  .coupon-scissors { position: absolute; left: 152px; top: 654px; }
  .coupon { position: absolute; left: 35px; top: 674px; width: 532px; height: 158px; }
  .coupon-shape { position: absolute; inset: 0; }
  .coupon-label {
    position: absolute; left: 60px; top: 23px; width: 36px; height: 108px;
    display: flex; align-items: center; justify-content: center;
  }
  .coupon-label span {
    transform: rotate(-90deg); font-family: "Montserrat", sans-serif; font-weight: 700;
    font-size: 17px; color: var(--paper); letter-spacing: 1px;
  }
  .coupon-title {
    position: absolute; left: 156px; top: 24px;
    font-family: "Montserrat", sans-serif; font-weight: 700; font-size: 17px; color: var(--ink);
  }
  .coupon-text {
    position: absolute; left: 156px; font-family: "Open Sans", sans-serif;
    font-size: 14px; color: var(--ink); white-space: nowrap;
  }
  .coupon-call { top: 52px; }
  .coupon-phone { font-weight: 700; font-size: 19px; color: var(--orange); margin-left: 3px; }
  .coupon-terms { top: 80px; }
  .coupon-tag {
    position: absolute; top: 106px; height: 32px; border-radius: 4px;
    background: var(--orange-dark); color: var(--paper);
    font-family: "Open Sans", sans-serif; font-weight: 700;
    display: flex; align-items: center; justify-content: center;
    box-shadow: 0 2px 3px rgba(0,0,0,.25);
  }
  .coupon-date { left: 158px; width: 106px; font-size: 14px; }
  .coupon-code { left: 278px; width: 188px; font-size: 17px; }
</style>
</head>
<body>
  <div class="ad">
    <svg class="ad-backdrop" width="603" height="867" viewBox="0 0 603 867" aria-hidden="true">
      <defs>
        <linearGradient id="sunburst" x1="0" y1="0" x2="1" y2="0">
          <stop offset="0" stop-color="#f5c419"/>
          <stop offset="0.5" stop-color="#f29a0e"/>
          <stop offset="1" stop-color="#ee8510"/>
        </linearGradient>
        <linearGradient id="chrome" x1="0" y1="0" x2="1" y2="0">
          <stop offset="0" stop-color="#9c9c9c"/>
          <stop offset="0.5" stop-color="#e6e6e6"/>
          <stop offset="1" stop-color="#b0b0b0"/>
        </linearGradient>
        <linearGradient id="paperfade" x1="0" y1="0" x2="0" y2="1">
          <stop offset="0" stop-color="#f1f1f1"/>
          <stop offset="1" stop-color="#ffffff"/>
        </linearGradient>
      </defs>
      <rect width="603" height="867" fill="var(--paper)"/>
      <polygon points="0,420 603,300 603,867 0,867" fill="url(#paperfade)"/>
      <polygon points="0,0 36,0 110,150 603,96 603,232 520,262 420,330 0,472" fill="url(#sunburst)"/>
      <polygon points="110,142 603,84 603,96 112,155" fill="url(#chrome)"/>
      <polygon points="520,222 570,262 420,300" fill="#bdbdbd"/>
      <polygon points="0,458 140,420 0,486" fill="url(#chrome)"/>
    </svg>

    <div class="brand">karosserie-lindenau.ch</div>

    <div class="car-visual" role="img" aria-label="Foto eines glänzenden roten Sportwagens in Dreiviertelansicht"></div>

    <h1 class="headline">WELLNESS</h1>
    <h2 class="subline">FÜR IHR AUTO</h2>
    <p class="lead">Ob kleinere Kratzer und Beulen oder ein grösseres Malheur,<br>wir verhelfen Ihrem Auto zu neuem Glanz!</p>

    <div class="coupon-cut"></div>
    <svg class="coupon-scissors" width="18" height="16" viewBox="0 0 18 16" aria-hidden="true">
      <circle cx="4" cy="4" r="3" fill="none" stroke="#777" stroke-width="1.5"/>
      <circle cx="4" cy="12" r="3" fill="none" stroke="#777" stroke-width="1.5"/>
      <line x1="6.5" y1="5.5" x2="17" y2="12" stroke="#777" stroke-width="1.5"/>
      <line x1="6.5" y1="10.5" x2="17" y2="4" stroke="#777" stroke-width="1.5"/>
    </svg>

    <div class="coupon">
      <svg class="coupon-shape" width="532" height="158" viewBox="0 0 532 158" aria-hidden="true">
        <rect width="532" height="158" fill="var(--orange)"/>
        <g fill="var(--paper)">
          <circle cx="0" cy="12" r="6"/><circle cx="0" cy="30" r="6"/><circle cx="0" cy="48" r="6"/>
          <circle cx="0" cy="66" r="6"/><circle cx="0" cy="84" r="6"/><circle cx="0" cy="102" r="6"/>
          <circle cx="0" cy="120" r="6"/><circle cx="0" cy="138" r="6"/>
          <circle cx="532" cy="12" r="6"/><circle cx="532" cy="30" r="6"/><circle cx="532" cy="48" r="6"/>
          <circle cx="532" cy="66" r="6"/><circle cx="532" cy="84" r="6"/><circle cx="532" cy="102" r="6"/>
          <circle cx="532" cy="120" r="6"/><circle cx="532" cy="138" r="6"/>
          <polygon points="44,13 478,13 500,40 500,145 44,145"/>
        </g>
        <polygon points="60,23 96,23 96,131 78,123 60,131" fill="var(--orange-dark)"/>
        <line x1="129" y1="20" x2="129" y2="138" stroke="var(--orange)" stroke-width="2"/>
      </svg>
      <div class="coupon-label"><span>COUPON</span></div>
      <div class="coupon-title">Gratis Hol- &amp; Bring-Service</div>
      <div class="coupon-text coupon-call">Rufen Sie uns an: Tel:<span class="coupon-phone">+41 55 410 62 30</span></div>
      <div class="coupon-text coupon-terms">Gültig im Umkreis von 50Km um Lindenau bis am</div>
      <div class="coupon-tag coupon-date">31. Dez. 2021</div>
      <div class="coupon-tag coupon-code">CODE: Reiseglanz</div>
    </div>
  </div>
</body>
</html>
```